Black Friday Sale - Banner

Black Friday Sale. for website
https://quenlodrift.com/
Our Black Friday sale includes a free product with a purchase of any flat iron.
banner size is 1880x720
Must include Black Friday Deal
Free Heat Protectant Spray with all purchases
Target Market(s)
Hair Care Professionals
Industry/Entity Type
Beauty Salon
Font styles to use
Sans Serif
Colors
86cae7
ec1f27
ffffff
Requirements
Must have
- Must have a photo image of the product that is free
Can include images of flat irons from website
Nice to have
- images from website
Should not have
- white person

```html
<!DOCTYPE html>
<html lang="en">
<head>
<meta charset="UTF-8">
<title>Black Friday Sale – Quenlo Drift</title>
<link rel="stylesheet" href="https://fonts.googleapis.com/css2?family=Montserrat:wght@300;800&family=Open+Sans:wght@400;700&family=Yellowtail&display=swap">
<style>
  :root {
    --bg-dark: #1e1f22;
    --bg-mid: #2c2d31;
    --brand-red: #ec1f27;
    --ribbon-red: #e0161d;
    --ribbon-deep: #b00d13;
    --white: #ffffff;
    --bottle-white: #f2f2f2;
    --bottle-orange: #f0582a;
    --ink: #111111;
  }
  * { margin: 0; padding: 0; box-sizing: border-box; }
  html, body {
    width: 1200px;
    height: 419px;
    overflow: hidden;
    background: var(--bg-dark);
  }
  .banner {
    position: relative;
    width: 1200px;
    height: 419px;
    overflow: hidden;
    background: radial-gradient(ellipse at 55% 45%, var(--bg-mid) 0%, var(--bg-dark) 75%);
    font-family: "Open Sans", sans-serif;
    color: var(--white);
  }
  .banner__frame {
    position: absolute;
    left: 11px;
    top: 11px;
    width: 1178px;
    height: 396px;
    border: 3px solid var(--white);
  }
  .gift-ribbon {
    position: absolute;
    left: 62px;
    top: 100px;
    width: 310px;
    height: 240px;
    border-radius: 16px;
    background: linear-gradient(160deg, var(--ribbon-red) 0%, var(--ribbon-deep) 100%);
  }
  .headline {
    position: absolute;
    left: 420px;
    width: 500px;
    text-align: center;
    font-family: "Montserrat", sans-serif;
    line-height: 1;
    white-space: nowrap;
  }
  .headline--black {
    top: 56px;
    font-size: 94px;
    font-weight: 800;
    color: var(--brand-red);
    letter-spacing: 0.3em;
    padding-left: 0.3em;
  }
  .headline--friday {
    top: 136px;
    font-size: 74px;
    font-weight: 300;
    color: var(--white);
    letter-spacing: 0.4em;
    padding-left: 0.4em;
  }
  .headline__script {
    position: absolute;
    left: 585px;
    top: 192px;
    width: 150px;
    text-align: center;
    font-family: "Yellowtail", cursive;
    font-size: 50px;
    line-height: 1;
    color: var(--brand-red);
  }
  .offer {
    position: absolute;
    left: 457px;
    top: 247px;
    width: 400px;
    text-align: center;
    font-size: 26px;
    line-height: 1.2;
    color: var(--white);
  }
  .gift-note {
    position: absolute;
    left: 412px;
    top: 310px;
    width: 500px;
    text-align: center;
  }
  .gift-note__free {
    display: block;
    font-family: "Montserrat", sans-serif;
    font-weight: 800;
    font-size: 40px;
    line-height: 1;
    color: var(--brand-red);
  }
  .gift-note__item {
    display: block;
    margin-top: 4px;
    font-size: 21px;
    line-height: 1.2;
    color: var(--white);
  }
  .product-shot {
    position: absolute;
    left: 955px;
    top: 65px;
    width: 153px;
    height: 268px;
    border-radius: 24px 24px 36px 36px;
    background: linear-gradient(180deg, var(--bottle-white) 0%, var(--bottle-white) 66%, var(--bottle-orange) 80%, var(--bottle-orange) 100%);
  }
  .cta {
    position: absolute;
    left: 1002px;
    top: 364px;
    width: 93px;
    height: 14px;
    background: var(--white);
    color: var(--ink);
    font-family: "Open Sans", sans-serif;
    font-size: 11px;
    line-height: 14px;
    text-align: center;
    text-decoration: none;
    letter-spacing: 0.02em;
  }
</style>
</head>
<body>
  <main class="banner">
    <div class="banner__frame"></div>

    <div class="gift-ribbon" role="img" aria-label="Red satin gift ribbon tied in a bow with a small sale tag"></div>

    <h1 class="headline headline--black">BLACK</h1>
    <p class="headline headline--friday">FRIDAY</p>
    <p class="headline__script">Sale</p>

    <p class="offer">save up to 50% off</p>

    <p class="gift-note">
      <span class="gift-note__free">FREE</span>
      <span class="gift-note__item">Heat Protectant Spray with all purchases</span>
    </p>

    <div class="product-shot" role="img" aria-label="Two white and orange thermal protectant spray bottles"></div>

    <a class="cta" href="https://quenlodrift.com/">GO SHOPPING</a>
  </main>
</body>
</html>
```